tiling company needs letterhead urgent

We need a logo to represent our company on an electronic letterhead. We are a tiling firm called Corliss Flooring Ltd and undertake all aspects of tiling work. The final design of the logo should incorporate the type of work we do and should be modern. We do not want any designs which may be considered 'novelty' or 'cartoonish.' No characters please, we require something sleek and contemporary . Please ensure the company name is central to your design ,Corliss Flooring Ltd

Industry/Entity Type

Electronic

Requirements
Must have
• text on letterhead to included

Registered address 58 Brindle grove Hapton Manchester M629QT
Company number 5273908
VAT no 741596238
Mobile no 07812649375
Office no 0161 548 7013
Web :www.surfacecraftexample.co.uk
Email : gerald@surfacecraftexample.co.uk
Nice to have
• a tile theme

```html
<!DOCTYPE html>
<html lang="en">
<head>
<meta charset="utf-8">
<title>Corliss Flooring Ltd – Letterhead</title>
<link rel="stylesheet" href="https://fonts.googleapis.com/css2?family=Questrial&display=swap">
<style>
  :root {
    --backdrop: #e9e9e9;
    --paper: #fbfbfb;
    --olive: #8d8646;
    --bronze: #5b4b31;
    --ink: #4a4a44;
  }
  * { margin: 0; padding: 0; box-sizing: border-box; }
  html, body {
    width: 1200px;
    height: 936px;
    overflow: hidden;
    background: var(--backdrop);
    font-family: "Questrial", "Century Gothic", sans-serif;
  }
  .letterhead {
    position: absolute;
    left: 290px;
    top: 30px;
    width: 620px;
    height: 876px;
    background: var(--paper);
    box-shadow: 0 2px 10px rgba(0,0,0,0.08);
  }
  .brand {
    position: absolute;
    left: 56px;
    top: 70px;
    display: flex;
    align-items: center;
    gap: 10px;
  }
  .brand-square {
    width: 18px;
    height: 18px;
    background: var(--olive);
  }
  .brand-block { display: flex; flex-direction: column; }
  .brand-name {
    font-size: 20px;
    letter-spacing: 2px;
    text-transform: uppercase;
    color: var(--bronze);
  }
  .brand-web {
    margin-top: 3px;
    font-size: 10px;
    color: var(--olive);
    letter-spacing: 0.5px;
  }
  .footer-contacts {
    position: absolute;
    left: 40px;
    right: 112px;
    bottom: 42px;
    display: flex;
    justify-content: space-between;
    align-items: center;
    font-size: 8px;
    color: var(--ink);
    white-space: nowrap;
  }
  .contact-list { display: flex; gap: 10px; }
  .contact-item { display: flex; align-items: center; gap: 3px; }
  .contact-icon { width: 8px; height: 8px; }
  .registration {
    position: absolute;
    right: 14px;
    bottom: 54px;
    text-align: right;
    font-size: 7px;
    line-height: 1.4;
    color: var(--ink);
  }
  .band-olive {
    position: absolute;
    left: 0;
    right: 100px;
    bottom: 22px;
    height: 10px;
    background: var(--olive);
  }
  .band-bronze {
    position: absolute;
    right: 0;
    width: 96px;
    bottom: 22px;
    height: 22px;
    background: var(--bronze);
  }
</style>
</head>
<body>
  <main class="letterhead">
    <header class="brand">
      <span class="brand-square"></span>
      <div class="brand-block">
        <span class="brand-name">Corliss Flooring Ltd</span>
        <span class="brand-web">www.surfacecraftexample.co.uk</span>
      </div>
    </header>

    <div class="registration">
      Company number 5273908<br>
      VAT 741596238
    </div>

    <footer class="footer-contacts">
      <span class="address">58 Brindle grove Hapton, Manchester M629QT</span>
      <span class="contact-list">
        <span class="contact-item">
          <svg class="contact-icon" viewBox="0 0 10 10"><circle cx="5" cy="5" r="5" fill="var(--olive)"/><rect x="3.5" y="2" width="3" height="6" rx="0.6" fill="#fff"/></svg>
          07812649375
        </span>
        <span class="contact-item">
          <svg class="contact-icon" viewBox="0 0 10 10"><circle cx="5" cy="5" r="5" fill="var(--olive)"/><path d="M3 2.5 L4.3 2.5 L4.8 4 L4 4.6 Q4.6 5.8 5.6 6.2 L6.2 5.4 L7.5 6 L7.5 7.3 Q4.5 7.5 3 4 Z" fill="#fff"/></svg>
          0161 548 7013
        </span>
        <span class="contact-item">
          <svg class="contact-icon" viewBox="0 0 10 10"><circle cx="5" cy="5" r="5" fill="var(--olive)"/><rect x="2.5" y="3.2" width="5" height="3.6" fill="#fff"/><path d="M2.5 3.2 L5 5.2 L7.5 3.2" stroke="var(--olive)" stroke-width="0.6" fill="none"/></svg>
          gerald@surfacecraftexample.co.uk
        </span>
      </span>
    </footer>

    <div class="band-olive"></div>
    <div class="band-bronze"></div>
  </main>
</body>
</html>
```